Business cards Dör Kornhüüs GmbH & Co.KG

We need a uniform business card design template for our employees.
A template should be created to have the same design for all business cards.

Contact Information for Business Card

Firma und Firmierung, Name, Funktion in Unternehmen, Anschrift, Tel. Handynummer, Emailadresse, Internetseite

Colors

Designer to choose colors to be used in the design.

Requirements
Must have
• Our company logo must be on it

```html
<!DOCTYPE html>
<html lang="de">
<head>
<meta charset="utf-8">
<title>Visitenkarte – Dör Kornhüüs GmbH &amp; Co.KG</title>
<link rel="stylesheet" href="https://fonts.googleapis.com/css2?family=Arimo:wght@400&display=swap">
<style>
  :root {
    --page: #ffffff;
    --card-border: #d9d9d9;
    --brand-pink: #ff4da6;
    --text-light: #ffffff;
  }
  html, body {
    margin: 0;
    padding: 0;
    width: 1200px;
    height: 1200px;
    overflow: hidden;
    background: var(--page);
    font-family: "Arimo", Arial, sans-serif;
  }
  .canvas {
    position: relative;
    width: 1200px;
    height: 1200px;
  }
  .business-card {
    position: absolute;
    left: 88px;
    top: 165px;
    width: 1035px;
    height: 592px;
    border: 1px solid var(--card-border);
    box-sizing: border-box;
    background: var(--page);
  }
  .contact-panel {
    position: absolute;
    left: 606px;
    top: 165px;
    width: 517px;
    height: 592px;
    background: var(--brand-pink);
  }
  .hexagon-divider {
    position: absolute;
    left: 0;
    top: 0;
    width: 1200px;
    height: 1200px;
    pointer-events: none;
  }
  .brand-name {
    position: absolute;
    left: 166px;
    top: 390px;
    margin: 0;
    font-size: 56px;
    font-weight: 400;
    line-height: 1;
    color: var(--brand-pink);
    white-space: nowrap;
  }
  .contact-field {
    position: absolute;
    left: 620px;
    margin: 0;
    font-size: 24px;
    line-height: 1;
    color: var(--text-light);
    white-space: nowrap;
  }
  .field-name     { top: 196px; }
  .field-role     { top: 279px; }
  .field-address  { top: 363px; left: 618px; }
  .field-phone    { top: 538px; }
  .field-mobile   { top: 594px; }
  .field-email    { top: 649px; }
  .field-web      { top: 705px; }
</style>
</head>
<body>
<main class="canvas">
  <section class="business-card" aria-label="Visitenkarte Vorderseite"></section>
  <section class="contact-panel" aria-label="Kontaktangaben"></section>

  <svg class="hexagon-divider" viewBox="0 0 1200 1200" aria-hidden="true">
    <polygon points="606,400 553,430 553,493 606,522" fill="var(--brand-pink)"/>
    <polygon points="606,400 658,430 658,493 606,522" fill="var(--page)"/>
  </svg>

  <p class="brand-name">Dör Kornhüüs</p>

  <p class="contact-field field-name">Name :</p>
  <p class="contact-field field-role">Funktion in Unternehmen :</p>
  <p class="contact-field field-address">Anschrift :</p>
  <p class="contact-field field-phone">Tel :</p>
  <p class="contact-field field-mobile">Handynummer :</p>
  <p class="contact-field field-email">Emailadresse :</p>
  <p class="contact-field field-web">Internetseite :</p>
</main>
</body>
</html>
```